Redesign Business Cards, Attached

Please read instructions carefully. If you have any questions send a message before submitting your ONE design. Please redesign attached business cards. Double sided. Use same content and descriptions. Use black, silver, crimson red and gold colors. My only issue with the attached design is the background colors. I like the layout as-is. I can provide the individual pictures on the back side later. Do not submit more than one design. One submission shall include both front and back. Do not submit front and back separately. A second project will be launched to create a matching post card after completion of this.
Industry/Entity Type
see description and attachments.
Contact Information for Business Card
Requirements
Must have
- see description and attachments.
Nice to have
Should not have

```html
<!DOCTYPE html>
<html lang="en">
<head>
<meta charset="utf-8">
<title>Helm &amp; Harbor – Business Card, Front and Back</title>
<link href="https://fonts.googleapis.com/css2?family=Fira+Sans:wght@400;600;700&family=Crimson+Text:wght@400;600&display=swap" rel="stylesheet">
<style>
  :root{
    --ink:#1f1d1e;
    --silver-light:#eeeeee;
    --silver-mid:#b9b9b9;
    --silver-dark:#8a8a8a;
    --gold:#c9a467;
    --crimson:#d40e54;
    --cream:#f4efe3;
    --white:#ffffff;
    --text-dark:#2a2a2a;
    --sea-dark:#3e4852;
    --sea-light:#9aa7b2;
  }
  *{margin:0;padding:0;box-sizing:border-box}
  html,body{width:922px;height:1200px;overflow:hidden;background:var(--white)}
  .sheet{position:relative;width:922px;height:1200px}
  .card{position:absolute;top:181px;width:374px;height:213px;display:block}
  .card--front{left:91px}
  .card--back{left:472px}
  .card-label{position:absolute;top:408px;font:700 12px "Fira Sans",sans-serif;color:var(--ink)}
  .card-label--front{left:91px}
  .card-label--back{left:472px}
  .swatches{position:absolute;left:90px;top:434px;display:flex;gap:5px}
  .swatch{width:23px;height:18px}
  .swatch--black{background:var(--ink)}
  .swatch--silver{background:linear-gradient(90deg,var(--silver-dark),var(--silver-light),var(--silver-dark))}
  .swatch--gold{background:linear-gradient(90deg,#9c7a45,#e6cc9a,#9c7a45)}
  .swatch--crimson{background:var(--crimson)}
  .service{font-family:"Fira Sans",sans-serif;font-size:7.4px;font-weight:600;fill:var(--white);text-anchor:middle}
  .web{font-family:"Fira Sans",sans-serif;font-weight:700;font-size:12px;fill:var(--white)}
  .brand{font-family:"Fira Sans",sans-serif;font-weight:700;font-size:7px;fill:var(--ink);text-anchor:middle}
  .name{font-family:"Fira Sans",sans-serif;font-weight:700;font-size:12.5px;fill:var(--white);letter-spacing:.3px}
  .title{font-family:"Crimson Text",serif;font-size:11.5px;fill:#d8d8d8}
  .phone{font-family:"Crimson Text",serif;font-size:16px;fill:#3a3a3a}
  .email{font-family:"Crimson Text",serif;font-size:7.5px;fill:#3a3a3a}
  .web--dark{fill:var(--text-dark);font-size:11.5px}
</style>
</head>
<body>
<main class="sheet">

  <svg class="card card--front" viewBox="0 0 374 213" xmlns="http://www.w3.org/2000/svg">
    <defs>
      <linearGradient id="front-sea" x1="0" x2="1" y1="0" y2="0">
        <stop offset="0" stop-color="#1f1d1e"/>
        <stop offset=".35" stop-color="#3e4852"/>
        <stop offset="1" stop-color="#9aa7b2"/>
      </linearGradient>
      <linearGradient id="front-band" x1="0" x2="1">
        <stop offset="0" stop-color="#5a5a5a"/>
        <stop offset=".5" stop-color="#f0f0f0"/>
        <stop offset="1" stop-color="#6a6a6a"/>
      </linearGradient>
    </defs>
    <rect class="card-base" width="374" height="213" fill="var(--ink)"/>
    <path class="card-photo" role="img" aria-label="Photo of a motor yacht cruising across open water" d="M140 0 L262 0 C270 80 300 150 336 213 L140 213 Z" fill="url(#front-sea)"/>
    <path class="top-band" d="M0 20 Q187 6 374 20 L374 38 Q187 26 0 38 Z" fill="url(#front-band)"/>
    <path class="swoosh-gold" d="M250 38 C258 110 290 170 324 213" fill="none" stroke="var(--gold)" stroke-width="2"/>
    <path class="swoosh-crimson" d="M258 38 C266 110 298 170 334 213" fill="none" stroke="var(--crimson)" stroke-width="6"/>
    <g class="brand-badge">
      <circle cx="149" cy="36" r="30" fill="var(--cream)" stroke="var(--gold)" stroke-width="3"/>
      <text class="brand" x="149" y="34">HELM &amp;</text>
      <text class="brand" x="149" y="43">HARBOR</text>
    </g>
    <g class="services">
      <g stroke="var(--crimson)" stroke-width="1.2">
        <line x1="59" y1="100" x2="59" y2="170"/>
        <line x1="112" y1="100" x2="112" y2="170"/>
        <line x1="168" y1="100" x2="168" y2="170"/>
      </g>
      <text class="service" x="33" y="106"><tspan x="33">Hands-On</tspan><tspan x="33" dy="10">Boat</tspan><tspan x="33" dy="10">Training</tspan></text>
      <text class="service" x="85" y="106"><tspan x="85">Introduction</tspan><tspan x="85" dy="10">to power</tspan><tspan x="85" dy="10">boating</tspan></text>
      <text class="service" x="140" y="106"><tspan x="140">Precision</tspan><tspan x="140" dy="10">Docking &amp;</tspan><tspan x="140" dy="10">Boat Handling</tspan></text>
      <text class="service" x="198" y="106"><tspan x="198">Open Water</tspan><tspan x="198" dy="10">Boat</tspan><tspan x="198" dy="10">Handling</tspan></text>
      <text class="service" x="33" y="142"><tspan x="33">Island</tspan><tspan x="33" dy="10">Anchoring</tspan></text>
      <text class="service" x="85" y="142"><tspan x="85">Open Water</tspan><tspan x="85" dy="10">Advanced</tspan><tspan x="85" dy="10">Maneuvers</tspan></text>
      <text class="service" x="140" y="142"><tspan x="140">Coastal</tspan><tspan x="140" dy="10">Navigation</tspan></text>
      <text class="service" x="198" y="142"><tspan x="198">Captaining</tspan><tspan x="198" dy="10">Piloting Service</tspan><tspan x="198" dy="10">for Your Outings</tspan></text>
    </g>
    <text class="web" x="174" y="198" text-anchor="middle">www.HireAHelm.com</text>
  </svg>

  <svg class="card card--back" viewBox="0 0 374 213" xmlns="http://www.w3.org/2000/svg">
    <defs>
      <linearGradient id="back-sea" x1="0" x2="1" y1="0" y2="1">
        <stop offset="0" stop-color="#a2aeb8"/>
        <stop offset=".6" stop-color="#5d6873"/>
        <stop offset="1" stop-color="#3a424a"/>
      </linearGradient>
      <linearGradient id="back-silver" x1="0" x2="1">
        <stop offset="0" stop-color="#d0d0d0"/>
        <stop offset=".5" stop-color="#f2f2f2"/>
        <stop offset="1" stop-color="#a8a8a8"/>
      </linearGradient>
    </defs>
    <rect class="card-base" width="374" height="213" fill="var(--ink)"/>
    <rect class="contact-band" x="0" y="145" width="374" height="68" fill="url(#back-silver)"/>
    <path class="card-photo" role="img" aria-label="Photo of a motor yacht cruising across open water" d="M0 0 L150 0 C136 70 112 140 96 213 L0 213 Z" fill="url(#back-sea)"/>
    <path class="swoosh-crimson" d="M154 0 C140 70 116 140 100 213" fill="none" stroke="var(--crimson)" stroke-width="6"/>
    <path class="swoosh-gold" d="M162 0 C148 70 124 140 108 213" fill="none" stroke="var(--gold)" stroke-width="2"/>
    <g class="brand-badge">
      <circle cx="133" cy="165" r="30" fill="var(--cream)" stroke="var(--gold)" stroke-width="3"/>
      <text class="brand" x="133" y="163">HELM &amp;</text>
      <text class="brand" x="133" y="172">HARBOR</text>
    </g>
    <text class="name" x="187" y="82">DANA R. HOLLOWAY</text>
    <text class="title" x="187" y="98">USCG Licensed Captain</text>
    <text class="title" x="187" y="112">Certified Instructor</text>
    <text class="phone" x="187" y="170">Text (555) 014-2290</text>
    <text class="email" x="187" y="185">hello@hireahelm.com</text>
    <text class="web web--dark" x="187" y="197">www.HireAHelm.com</text>
  </svg>

  <span class="card-label card-label--front">front</span>
  <span class="card-label card-label--back">back</span>
  <div class="swatches">
    <span class="swatch swatch--black"></span>
    <span class="swatch swatch--silver"></span>
    <span class="swatch swatch--gold"></span>
    <span class="swatch swatch--crimson"></span>
  </div>

</main>
</body>
</html>
```